New Year Resolution Infographic

We are a weight loss company that provides holistic, natural nutrition programs to consumers -- you can see our Web site at www.TrimLark.com We need a simple infographic to be shared on social media and via email for New Year's day. The topic for the infographic is "how to set and keep your weight loss resolution". We've outlined 5 process steps for consumers to follow to assist with their weight loss resolutions, and we would like to depict this graphically.

Target Market(s)

Women age 35-65 who are planning to make a resolution to lose weight in the new year.

Industry/Entity Type

Health And Wellness

Font styles to use
Sans Serif

Colors
0392cd
9bcb3c

Requirements
Must have
• Initial graphic showing failure stats (see copy)
• Graphic showing process steps in making/keeping a resolution (see copy)
• TrimLark Logo

```html
<!DOCTYPE html>
<html lang="en">
<head>
<meta charset="utf-8">
<title>TrimLark – How to Set and Reach Your Weight Loss Resolution</title>
<link rel="stylesheet" href="https://fonts.googleapis.com/css2?family=Raleway:wght@300;400&family=Montserrat:wght@400;800;900&display=swap">
<style>
  :root {
    --brand-blue: #1da9e1;
    --brand-green: #9bbd3b;
    --reflect-orange: #e9592d;
    --resolve-blue: #1da9e1;
    --replace-green: #9bbd3b;
    --record-blue: #3bb3e3;
    --reward-dark: #333333;
    --body-grey: #555555;
    --panel-grey: #f1f1f1;
    --panel-grey-dark: #e9e9e9;
    --white: #ffffff;
  }
  * { margin: 0; padding: 0; box-sizing: border-box; }
  html, body { width: 1200px; height: 675px; overflow: hidden; background: var(--white); }
  .canvas { position: relative; width: 1200px; height: 675px; overflow: hidden; font-family: "Raleway", sans-serif; }
  .backdrop { position: absolute; inset: 0; }
  .brand {
    position: absolute; left: 38px; top: 28px;
    font-family: "Montserrat", sans-serif; font-weight: 400;
    font-size: 58px; letter-spacing: -1px; color: var(--brand-blue);
  }
  .headline {
    position: absolute; left: 40px; top: 210px; width: 490px;
    text-align: center; text-transform: uppercase; line-height: 1;
  }
  .headline .light { display: block; font-family: "Raleway", sans-serif; font-weight: 300; color: var(--brand-green); font-size: 52px; letter-spacing: 1px; }
  .headline .heavy { display: block; font-family: "Montserrat", sans-serif; font-weight: 900; color: var(--brand-blue); font-size: 64px; letter-spacing: 1px; }
  .headline .light.first { font-size: 46px; margin-bottom: 4px; }
  .headline .heavy + .light { margin-top: 2px; }
  .step { position: absolute; display: flex; align-items: flex-start; }
  .step-badge { width: 106px; height: 106px; border-radius: 50%; flex: none; display: flex; align-items: center; justify-content: center; }
  .step-copy { margin-left: 18px; width: 470px; }
  .step-title { font-family: "Raleway", sans-serif; font-weight: 300; font-size: 35px; line-height: 1; text-transform: uppercase; margin-bottom: 4px; }
  .step-text { font-family: "Raleway", sans-serif; font-weight: 400; font-size: 16px; line-height: 1.5; color: var(--body-grey); }
  .step--reflect { left: 498px; top: 14px; }
  .step--reflect .step-badge { background: var(--reflect-orange); }
  .step--reflect .step-title { color: var(--reflect-orange); margin-top: 16px; }
  .step--resolve { left: 581px; top: 132px; }
  .step--resolve .step-badge { background: var(--resolve-blue); }
  .step--resolve .step-title { color: var(--resolve-blue); }
  .step--replace { left: 599px; top: 273px; }
  .step--replace .step-badge { background: var(--replace-green); }
  .step--replace .step-title { color: var(--replace-green); }
  .step--record { left: 574px; top: 424px; }
  .step--record .step-badge { background: var(--record-blue); }
  .step--record .step-title { color: var(--record-blue); }
  .step--reward { left: 499px; top: 552px; }
  .step--reward .step-badge { background: var(--reward-dark); }
  .step--reward .step-title { color: var(--reward-dark); }
  .question-mark { font-family: "Montserrat", sans-serif; font-weight: 800; font-size: 66px; color: var(--white); line-height: 1; }
</style>
</head>
<body>
<main class="canvas">
  <svg class="backdrop" width="1200" height="675" viewBox="0 0 1200 675" aria-hidden="true">
    <circle cx="-70" cy="340" r="570" fill="var(--panel-grey)"/>
    <path d="M0 0 H380 A570 570 0 0 1 470 110 Q240 40 0 110 Z" fill="var(--panel-grey-dark)"/>
    <path d="M525 640 Q495 655 470 675" fill="none" stroke="var(--brand-blue)" stroke-width="1.2"/>
  </svg>

  <div class="brand">TRIMLARK</div>

  <h1 class="headline">
    <span class="light first">How to set and</span>
    <span class="heavy">Reach your</span>
    <span class="light">Weight loss</span>
    <span class="heavy">Resolution</span>
  </h1>

  <section class="step step--reflect">
    <div class="step-badge"><span class="question-mark">?</span></div>
    <div class="step-copy">
      <h2 class="step-title">Reflect</h2>
      <p class="step-text">Get clear on why the achievement of your resolution is important.&nbsp; You’ll need to come back to this if you falter!</p>
    </div>
  </section>

  <section class="step step--resolve">
    <div class="step-badge">
      <svg width="70" height="70" viewBox="0 0 70 70" aria-hidden="true">
        <g fill="none" stroke="#fff" stroke-width="4">
          <circle cx="40" cy="30" r="24"/><circle cx="40" cy="30" r="15"/><circle cx="40" cy="30" r="6"/>
        </g>
        <line x1="40" y1="30" x2="12" y2="58" stroke="#fff" stroke-width="4"/>
        <path d="M6 52 L14 50 L20 56 L18 64 Z" fill="#fff"/>
      </svg>
    </div>
    <div class="step-copy">
      <h2 class="step-title">Resolve</h2>
      <p class="step-text">Set a weight loss goal for the year that is realistic, then break this up into even shorter term goals of 30-60 days, with a specific diet and activity plan to guide you.</p>
    </div>
  </section>

  <section class="step step--replace">
    <div class="step-badge">
      <svg width="70" height="50" viewBox="0 0 70 50" aria-hidden="true">
        <g fill="none" stroke="#222" stroke-width="6">
          <path d="M2 12 H18 C32 12 34 38 50 38 H58"/>
          <path d="M2 38 H18 C32 38 34 12 50 12 H58"/>
        </g>
        <path d="M56 2 L68 12 L56 22 Z M56 28 L68 38 L56 48 Z" fill="#222"/>
      </svg>
    </div>
    <div class="step-copy">
      <h2 class="step-title">Replace</h2>
      <p class="step-text">Clear out your pantry and stock up with only healthy foods.&nbsp; Then work to build new activity and eating habits that take the place of your current habits.</p>
    </div>
  </section>

  <section class="step step--record">
    <div class="step-badge">
      <svg width="80" height="60" viewBox="0 0 80 60" aria-hidden="true">
        <polyline points="6,52 20,38 32,42 44,28 54,32 70,12" fill="none" stroke="#fff" stroke-width="2"/>
        <path d="M66 8 L76 6 L73 16 Z" fill="#fff"/>
        <g fill="var(--record-blue)" stroke="#fff" stroke-width="2">
          <circle cx="20" cy="38" r="3"/><circle cx="32" cy="42" r="3"/><circle cx="44" cy="28" r="3"/><circle cx="54" cy="32" r="3"/>
        </g>
      </svg>
    </div>
    <div class="step-copy">
      <h2 class="step-title">Record</h2>
      <p class="step-text">Track your progress daily, tell your family and friends about your resolution to create more accountability, and recruit a partner to share your journey.</p>
    </div>
  </section>

  <section class="step step--reward">
    <div class="step-badge">
      <svg width="60" height="80" viewBox="0 0 60 80" aria-hidden="true">
        <path d="M18 40 L12 76 L22 68 L28 76 L30 44 Z M42 40 L48 76 L38 68 L32 76 L30 44 Z" fill="#c0282d"/>
        <circle cx="30" cy="28" r="22" fill="#efe6d6"/>
        <circle cx="30" cy="28" r="14" fill="#c7b48f"/>
      </svg>
    </div>
    <div class="step-copy">
      <h2 class="step-title">Reward</h2>
      <p class="step-text">Rather than using unhealthy food as a reward or cheat, give yourself healthy or relaxing experiences – such a spa treatment or taking a new fitness class.</p>
    </div>
  </section>
</main>
</body>
</html>
```